Modern CNC Machining Facility in Need of Web Site Improvement

Brightmoor Fabrication and Tooling, LLC is in need of a web site update. We need to highlight both product sales and our manufacturing services offered. We have recently started offering online product sales and need a better ecommerce platform for our customers. We would like the design winner to be able to freelance the project to a fully functioning webpage.
www.brightmoorfab.example
What we like about our current web site:
Black and red highlight colors
Gear and caliper logo
USMC Veteran owned business
What we don't like about our current web site:
Unorganized
Doesn't stand out
Looks like it was made in 1995
Online Product sales are awkward

```html
<!DOCTYPE html>
<html lang="en">
<head>
<meta charset="utf-8">
<title>Brightmoor Fabrication and Tooling, LLC</title>
<link rel="stylesheet" href="https://fonts.googleapis.com/css2?family=Arimo:wght@400;700&display=swap">
<style>
  :root {
    --brand-red: #a3191d;
    --ink: #111;
    --body-grey: #555;
    --frame: #d4d4d4;
    --tab-edge: #e2e2e2;
    --hero-bg: #efefef;
    --hero-stripe: #e6e6e6;
    --card-bg: #f3f3ee;
    --card-edge: #c9c9c4;
    --dot-off: #d3d3d3;
    --logo-dark: #232021;
  }
  * { box-sizing: border-box; margin: 0; padding: 0; }
  html, body { width: 1200px; height: 1090px; overflow: hidden; background: #fff; }
  body { font-family: "Arimo", Arial, sans-serif; color: var(--ink); position: relative; }

  .site-frame {
    position: absolute; left: 18px; top: 1px; width: 1164px; height: 1055px;
    border: 2px solid var(--frame); border-top-width: 1px;
  }

  .brand-mark {
    position: absolute; left: 33px; top: 16px; width: 164px; height: 164px; z-index: 3;
    border-radius: 50%; background: var(--logo-dark);
    display: flex; align-items: center; justify-content: center;
  }
  .brand-mark span { color: #fff; font-size: 21px; font-weight: 400; }

  .main-nav { position: absolute; top: 1px; left: 204px; height: 82px; display: flex; z-index: 2; }
  .nav-tab {
    height: 82px; display: flex; align-items: center; justify-content: center; text-align: center;
    font-size: 16.5px; line-height: 19px; color: var(--ink); white-space: nowrap;
    border-left: 2px solid var(--tab-edge); border-right: 2px solid var(--tab-edge);
    background: #fff; margin-right: 2px;
  }
  .nav-tab.is-current { background: linear-gradient(#fdfdfd, #e6e6e6); border-bottom: 2px solid #ccc; }
  .nav-tab.tab-blog { font-size: 16px; }

  .site-search {
    position: absolute; left: 961px; top: 35px; width: 190px; height: 27px; z-index: 2;
    border: 1px solid #d6d6d6; border-radius: 14px; background: #fff;
    display: flex; align-items: center; font-size: 13px; color: #c5c5c5;
  }
  .site-search svg { margin: 0 6px; }
  .site-search .divider { width: 1px; height: 25px; background: #e0e0e0; margin-right: 10px; }

  .hero {
    position: absolute; left: 20px; top: 88px; width: 1160px; height: 510px;
    background: var(--hero-bg);
  }
  .hero-title {
    position: absolute; left: 30px; top: 150px; width: 360px; text-align: center;
    color: var(--brand-red); font-size: 32px; line-height: 42px; font-weight: 400;
    white-space: nowrap;
  }
  .hero-machine {
    position: absolute; left: 402px; top: 15px; width: 388px; height: 489px;
    background: linear-gradient(#e4e4e2 0%, #d8d8d6 45%, #8f939b 60%, #7f838c 100%);
    border-radius: 4px;
  }

  .slide-dots { position: absolute; top: 606px; left: 532px; display: flex; gap: 5px; }
  .slide-dots span { width: 18px; height: 18px; border-radius: 50%; background: var(--dot-off); }
  .slide-dots span.is-active { background: var(--brand-red); }

  .feature-card {
    position: absolute; top: 686px; width: 261px; height: 219px;
    background: var(--card-bg); border: 1px solid var(--card-edge);
    box-shadow: 0 2px 4px rgba(0,0,0,0.12);
  }
  .feature-card .curl { position: absolute; width: 28px; height: 46px; }
  .feature-card .curl-top { left: -1px; top: -1px; }
  .feature-card .curl-bottom { right: -1px; bottom: -1px; transform: rotate(180deg); }
  .feature-card h2 { position: absolute; left: 29px; top: 30px; font-size: 21px; font-weight: 400; }
  .feature-card .card-body {
    position: absolute; left: 31px; top: 72px; width: 205px; height: 86px; overflow: hidden;
    font-size: 14.2px; line-height: 17px; color: var(--body-grey);
  }
  .feature-card .card-body strong { color: var(--ink); font-weight: 700; display: block; white-space: nowrap; }
  .feature-card .read-more {
    position: absolute; left: 31px; font-size: 13.5px; color: var(--brand-red); text-decoration: underline;
  }
  .card-about { left: 76px; }
  .card-about .card-body { top: 70px; height: 101px; }
  .card-about .read-more { top: 178px; }
  .card-products { left: 462px; }
  .card-products .read-more { top: 166px; }
  .card-spears { left: 845px; }
  .card-spears h2 { top: 27px; }
  .card-spears .card-body { top: 69px; }
  .card-spears .read-more { top: 165px; }

  .site-footer {
    position: absolute; left: 20px; top: 1006px; width: 1160px; border-top: 1px solid #dedede;
  }
  .site-footer p { position: absolute; right: 78px; top: 15px; font-size: 14.2px; white-space: nowrap; }
  .site-footer .footer-brand { color: var(--brand-red); font-weight: 700; }
</style>
</head>
<body>
  <div class="site-frame"></div>

  <div class="brand-mark"><span>Brightmoor</span></div>

  <nav class="main-nav">
    <a class="nav-tab" style="width:78px">Home</a>
    <a class="nav-tab is-current" style="width:111px">Online<br>Product<br>Sale</a>
    <a class="nav-tab" style="width:88px">Ice<br>Fishing<br>Spears</a>
    <a class="nav-tab" style="width:74px">About<br>Us</a>
    <a class="nav-tab" style="width:102px">Equipment</a>
    <a class="nav-tab" style="width:91px">Contact<br>Us</a>
    <a class="nav-tab tab-blog" style="width:186px">Brightmoor Fabrication<br>Blog</a>
  </nav>

  <div class="site-search">
    <svg width="16" height="16" viewBox="0 0 16 16"><circle cx="6.5" cy="6.5" r="4.5" fill="none" stroke="#bbb" stroke-width="1.6"/><line x1="10" y1="10" x2="14.5" y2="14.5" stroke="#bbb" stroke-width="2"/></svg>
    <span class="divider"></span>Search...
  </div>

  <section class="hero">
    <h1 class="hero-title">Brightmoor Fabrication<br>and<br>Tooling, LLC</h1>
    <div class="hero-machine" role="img" aria-label="Photo of a compact CNC lathe with grey cabinet and control panel"></div>
  </section>

  <div class="slide-dots"><span></span><span class="is-active"></span><span></span><span></span><span></span></div>

  <article class="feature-card card-about">
    <svg class="curl curl-top" viewBox="0 0 28 46"><path d="M0 0 H28 C12 4 4 20 0 46 Z" fill="#a3191d"/></svg>
    <svg class="curl curl-bottom" viewBox="0 0 28 46"><path d="M0 0 H28 C12 4 4 20 0 46 Z" fill="#a3191d"/></svg>
    <h2>About Us</h2>
    <div class="card-body"><strong>About Brightmoor Fabrication</strong>"Our company is based on the belief that our customers' needs are of the utmost importance. Our entire team at Brightmoor Fabrication is committed</div>
    <a class="read-more">Read more...</a>
  </article>

  <article class="feature-card card-products">
    <svg class="curl curl-top" viewBox="0 0 28 46"><path d="M0 0 H28 C12 4 4 20 0 46 Z" fill="#a3191d"/></svg>
    <svg class="curl curl-bottom" viewBox="0 0 28 46"><path d="M0 0 H28 C12 4 4 20 0 46 Z" fill="#a3191d"/></svg>
    <h2>Products</h2>
    <div class="card-body">We carry a wide range of products to suit a variety of budgets and tastes. Our most popular products are shown below.</div>
    <a class="read-more">Read more...</a>
  </article>

  <article class="feature-card card-spears">
    <svg class="curl curl-top" viewBox="0 0 28 46"><path d="M0 0 H28 C12 4 4 20 0 46 Z" fill="#a3191d"/></svg>
    <svg class="curl curl-bottom" viewBox="0 0 28 46"><path d="M0 0 H28 C12 4 4 20 0 46 Z" fill="#a3191d"/></svg>
    <h2>Ice Fishing Spears</h2>
    <div class="card-body">We believe that our ice fishing spears are the best fishing spears on the market.&nbsp; Each spear has been meticulously manufactured with pride and</div>
    <a class="read-more">Read more...</a>
  </article>

  <footer class="site-footer">
    <p>Copyright © 2014 <span class="footer-brand">Brightmoor Fabrication and Tooling, LLC</span> Privacy Policy | Terms &amp; Conditions</p>
  </footer>
</body>
</html>
```